SEO Agentur www.findeprofi.de - Webseite soll neu designed werden (Start- und Unterseite)
Zielgruppe
Alle Infos sind auf der Seite www.findeprofi.de enthalten.
Aufgabenstellung
Die Seite soll neu gestalltet werden. Wir möchten gerne ein wenig professioneller werden. Der Name der Seite zwingt uns allerdings ein gewisses Thema auf.
Die Aufgabe:
Ein professionelleres Design der Startseite und einer Unterseite. Die Programmierung machen wir selbst. Thema Suche und Helden muss bleiben aufgrund der URL.
Mit dem Gewinner würden wir dann auch geren jedes Element der Seite durchgehen und neu gestallten (separater Auftrag).
Das Blitzwolf Logo ist aufgrund des neuen Films auch gewaltiger und seriöser geworden. Vielleicht kann man daran anknüpfen. Ist aber keine Bedingung nur eine kleine Idee.
Wir werden alle Vorschläge ca. 50 Leuten vorstellen und dann den Vorschlag mit den meisten Stimmen wählen.

```html
<!DOCTYPE html>
<html lang="de">
<head>
<meta charset="utf-8">
<title>findeprofi.de – SEO Agentur</title>
<link href="https://fonts.googleapis.com/css2?family=Jost:wght@300;400&family=Roboto+Slab:wght@300;400&family=Signika:wght@600&family=Arimo:wght@400;700&display=swap" rel="stylesheet">
<style>
:root{
  --cyan:#00c3ee;
  --cyan-dark:#0b6f88;
  --black:#000;
  --header:#161616;
  --band:#1c1c1e;
  --white:#fff;
  --text-dark:#222;
  --red:#e0232d;
}
*{margin:0;padding:0;box-sizing:border-box}
html,body{width:1086px;height:1200px;overflow:hidden;background:var(--black)}
.page{position:relative;width:1086px;height:1200px;overflow:hidden;font-family:'Jost',sans-serif;color:var(--white)}
.abs{position:absolute}

/* header */
.site-header{left:0;top:0;width:1086px;height:120px;background:var(--header)}
.brand{left:18px;top:40px;display:flex;align-items:center;gap:7px;font:400 17px 'Jost',sans-serif;color:var(--white)}
.brand-mark{width:14px;height:14px;background:#f2d31b}
.main-nav{left:250px;top:42px;display:flex;font:400 19px 'Jost',sans-serif}
.main-nav a{color:var(--white);text-decoration:none;margin-right:19px}
.main-nav a.active{color:var(--cyan)}

/* hero */
.hero-visual{left:0;top:120px;width:1086px;height:380px;background:radial-gradient(ellipse at 50% 30%,#8a8a8a 0%,#4e4e4e 40%,#262626 85%)}
.hero-title{left:250px;top:219px;width:540px;text-align:center;font:300 62px/52px 'Roboto Slab',serif;color:var(--cyan);border-top:3px solid var(--cyan);border-bottom:3px solid var(--cyan);padding:6px 0 4px;letter-spacing:1px}

/* services */
.services{left:0;top:500px;width:1086px;height:219px;background:var(--band)}
.section-title{width:1086px;text-align:center;font:400 32px 'Roboto Slab',serif;color:var(--white)}
.gem-label{font:300 21px 'Jost',sans-serif;fill:var(--white)}
.pointer{left:506px;top:695px;width:0;height:0;border-left:24px solid transparent;border-right:24px solid transparent;border-bottom:24px solid var(--white)}
.services-intro{left:0;top:719px;width:1086px;height:62px;background:var(--white)}
.services-intro p{position:absolute;left:143px;top:11px;width:860px;font:300 13.5px/14px 'Jost',sans-serif;color:var(--text-dark);text-align:justify;text-align-last:center}
.services-intro a{color:var(--cyan);text-decoration:none}

/* about */
.about-title{top:796px}
.col-heading{font:400 17px 'Roboto Slab',serif;color:var(--cyan)}
.col-text{font:600 14px/18.7px 'Signika',sans-serif;color:var(--white)}
.about-clip{left:0;top:781px;width:1086px;height:277px;overflow:hidden}
.divider{left:526px;top:846px;width:2px;height:212px;background:var(--cyan-dark)}
.art{background:radial-gradient(circle,#3a3a3a 0%,#111 70%)}
.art-right{float:right;width:170px;height:125px;margin:0 0 4px 12px;background:radial-gradient(circle at 45% 45%,#2a6f85 0%,#1a1a1a 70%)}

/* footer */
.site-footer{left:0;top:1058px;width:1086px;height:142px;background:linear-gradient(#1e1e1e,#101010);border-top:2px solid #4a90b8}
.footer-name{left:205px;top:1076px;font:400 17px 'Roboto Slab',serif;color:var(--cyan)}
.footer-address{left:204px;top:1100px;font:400 11px/15.5px 'Arimo',sans-serif;color:var(--white)}
.footer-col{top:1070px;font:400 10.5px 'Arimo',sans-serif;color:var(--white)}
.footer-col h4{font:700 11px 'Arimo',sans-serif;margin-bottom:9px}
.footer-col li{list-style:none;margin-bottom:8.3px}
.footer-btn{top:1180px;height:22px;width:136px;background:var(--cyan);clip-path:polygon(14% 0,86% 0,100% 100%,0 100%);font:400 10.5px/22px 'Arimo',sans-serif;text-align:center;color:var(--white)}
</style>
</head>
<body>
<div class="page">

  <header class="site-header abs">
    <div class="brand abs"><span class="brand-mark"></span>findeprofi.de</div>
    <nav class="main-nav abs">
      <a class="active" href="#">Ablauf</a>
      <a href="#">Ihre Vorteile</a>
      <a href="#">Unsere Leistungen</a>
      <a href="#">100% Geld-zurück-Garantie</a>
      <a href="#">Infos</a>
      <a href="#">Blog</a>
      <a href="#" style="margin-right:0">Kontakt</a>
    </nav>
  </header>

  <div class="hero-visual abs" role="img" aria-label="Schwarzweiß-Foto: Mann im Anzug reißt sein Hemd auf, rote Krawatte"></div>
  <h1 class="hero-title abs">IHRE WEBSITE<br>GANZ OBEN!</h1>

  <section class="services abs">
    <h2 class="section-title abs" style="top:4px">SERVICES</h2>
    <svg class="abs" style="left:0;top:0" width="1086" height="219" viewBox="0 0 1086 219">
      <!-- Webdesign -->
      <polygon points="256,64 378,64 394,84 317,183 240,84" fill="var(--cyan-dark)"/>
      <text class="gem-label" x="317" y="86" text-anchor="middle">Webdesign</text>
      <rect x="300" y="100" width="28" height="34" fill="none" stroke="#b8323c" stroke-width="3"/>
      <line x1="312" y1="132" x2="340" y2="104" stroke="#b8323c" stroke-width="6"/>
      <!-- SEO -->
      <polygon points="456,52 600,52 617,72 528,189 439,72" fill="var(--cyan)"/>
      <text class="gem-label" x="528" y="74" text-anchor="middle" style="font-size:23px">SEO</text>
      <circle cx="528" cy="122" r="26" fill="none" stroke="var(--red)" stroke-width="5"/>
      <ellipse cx="528" cy="122" rx="11" ry="26" fill="none" stroke="var(--red)" stroke-width="4"/>
      <line x1="502" y1="122" x2="554" y2="122" stroke="var(--red)" stroke-width="4"/>
      <polygon points="533,116 533,150 541,142 548,156 553,153 546,139 557,139" fill="#111" stroke="var(--cyan)" stroke-width="1.5"/>
      <!-- Social SEO -->
      <polygon points="683,64 805,64 821,84 744,183 667,84" fill="var(--cyan-dark)"/>
      <text class="gem-label" x="744" y="86" text-anchor="middle">Social SEO</text>
      <path d="M744,140 L724,120 A10,10 0 0 1 744,106 A10,10 0 0 1 764,120 Z" fill="none" stroke="#b8323c" stroke-width="4"/>
      <rect x="751" y="118" width="6" height="24" fill="#222"/>
      <rect x="742" y="127" width="24" height="6" fill="#222"/>
    </svg>
  </section>
  <div class="pointer abs"></div>

  <section class="services-intro abs">
    <p>Rund 40% der User klicken bei Suchmaschinen wie Findly, Seeko und Quero auf die Interseite, welche bei dem entsprechenden Keyword auf Platz 1 gerankt wird. Das es pro Keyword leider immer nur einen ersten Platz zu vergeben gibt, stellt dies Websitebetreiber vor die schwierige Aufgabe, bei Findly &amp; Co. mit Ihrer Internetseite auf Platz 1 gerankt zu werden… <a href="#">(mehr)</a></p>
  </section>

  <section class="about-clip abs">
    <h2 class="section-title abs" style="top:15px">ABOUT</h2>
    <div class="art abs" style="left:58px;top:76px;width:144px;height:144px;border-radius:50%" role="img" aria-label="Kreisdiagramm der SEO-Schritte mit Pfeilen und Symbolen"></div>
    <div class="abs" style="left:255px;top:62px;width:240px">
      <h3 class="col-heading">SEO (organisch)</h3>
      <p class="col-text" style="margin-top:13px">Suchmaschinenoptimierung ist die effizienteste und günstigste Art, im Internet neue Kunden zu bekommen. Wir von Findeprofi.de positionieren ausgewählte Suchbegriffe ganz oben bei Suchdiensten wie Findly &amp; Co.! Mit Hilfe unserer Dienstleistung werden potentielle Kunden deutlich eher auf Sie aufmerksam und Sie machen mehr Umsatz.</p>
    </div>
    <div class="abs" style="left:562px;top:62px;width:410px">
      <h3 class="col-heading">Unsere Garantie für Sie:</h3>
      <div class="col-text" style="margin-top:13px;padding-left:3px">
        <div class="art-right" role="img" aria-label="Wortwolke mit SEO-Begriffen unter einer Lupe"></div>
        Sollten Ihre vorab festgelegten Suchbegriffe gegen alle Erwartungen nicht innerhalb von 6 Monaten unter den TOP 10 bei den Suchergebnissen von Findly gelistet sein, erhalten Sie von uns rückwirkend zu 100% Ihr Geld zurück - garantiert! Testen Sie uns und lassen Sie sich von unserer Erfahrung und unserem Know-How beeindrucken. Wir halten, was andere versprechen!
      </div>
    </div>
  </section>
  <div class="divider abs"></div>

  <footer class="site-footer abs"></footer>
  <svg class="abs" style="left:17px;top:1058px" width="182" height="142" viewBox="0 0 182 142" role="img" aria-label="Kartenausschnitt mit Standortmarkierung">
    <polygon points="91,0 182,0 91,132 0,28 24,0" fill="#d9dcd3" stroke="var(--red)" stroke-width="2"/>
  </svg>
  <div class="footer-name abs">Findeprofi.de GbR</div>
  <div class="footer-address abs">Lindenweg 4<br>49100 Musterstadt</div>

  <div class="footer-col abs" style="left:446px"><h4>Menü</h4><ul><li>Über uns</li><li>Ihre Vorteile</li><li>Wie es funktioniert?</li><li>100% Geld-zurück-Garantie</li><li>Kontakt</li></ul></div>
  <div class="footer-col abs" style="left:604px"><h4>Suchmaschinenoptimierung</h4><ul><li>SEO Agentur</li><li>SEO Marketing</li><li>SEO Umsatz</li><li>Suchmaschinenoptimierung Agentur</li><li>SEO Agentur Erfolgsbasiert</li></ul></div>
  <div class="footer-col abs" style="left:807px"><h4>Suchmaschinenwerbung</h4><ul><li>Findly Ads Agentur</li><li>Findly Ads</li><li>SEA Agentur</li><li>SEM Agentur</li></ul></div>
  <div class="footer-col abs" style="left:983px"><h4>Erklärvideos</h4><ul><li>Erklärvideos</li><li>Erklärfilme</li><li>Produktvideos</li></ul></div>

  <div class="footer-btn abs" style="left:795px">Impressum</div>
  <div class="footer-btn abs" style="left:923px">Zum Kontaktformular</div>
</div>
</body>
</html>
```